Structural Engineering Business Card

Veltrow Drafts does residential house plans for clients in Central Florida. Would like simple but elegant business card that is appropriate for a house plan engineering company. Prefer black business card with black/white them but open to other shades of blue. I uploaded a sample card that I came across that looked good but please come up with your own creative designs.

Contact Information for Business Card

Name, Title, Phone, Email, Address, website

```html
<!DOCTYPE html>
<html lang="en">
<head>
<meta charset="utf-8">
<title>Veltrow Drafts — Business Card</title>
<link rel="stylesheet" href="https://fonts.googleapis.com/css2?family=Lato:wght@400;700;900&display=swap">
<style>
  :root {
    --page: #e6e4e1;
    --card: #1b1b1b;
    --card-edge: #262626;
    --ink: #ffffff;
    --ink-soft: #e9e9e9;
    --drawing-1: #2a2d31;
    --drawing-2: #1b1b1b;
  }
  * { margin: 0; padding: 0; box-sizing: border-box; }
  html, body {
    width: 1200px; height: 992px; overflow: hidden;
    background: var(--page);
    font-family: "Lato", sans-serif;
  }
  .sheet {
    position: relative; width: 1200px; height: 992px;
    display: flex; flex-direction: column; align-items: center;
    justify-content: center; gap: 64px;
  }
  .card {
    position: relative; width: 620px; height: 354px;
    background: var(--card);
    border-radius: 22px;
    overflow: hidden;
    color: var(--ink);
    box-shadow: 0 10px 28px rgba(0,0,0,0.22);
  }
  /* front */
  .card-front .elevation-drawing {
    position: absolute; right: 0; top: 0; width: 64%; height: 100%;
    background: radial-gradient(ellipse at 60% 60%, var(--drawing-1) 0%, var(--drawing-2) 75%);
  }
  .card-front .wordmark {
    position: absolute; left: 0; right: 0; top: 50%;
    transform: translateY(-50%);
    display: flex; align-items: center; justify-content: center; gap: 16px;
  }
  .wordmark-mark { width: 22px; height: 22px; background: var(--ink); border-radius: 50%; }
  .wordmark-name {
    font-weight: 900; font-size: 54px; letter-spacing: 1px;
    line-height: 1; text-transform: uppercase;
  }
  /* back */
  .card-back { display: flex; align-items: center; }
  .card-back .brand {
    width: 46%; display: flex; align-items: center; justify-content: center; gap: 10px;
  }
  .card-back .wordmark-mark { width: 14px; height: 14px; }
  .card-back .wordmark-name { font-size: 27px; }
  .divider { width: 2px; height: 200px; background: var(--ink-soft); }
  .contact { padding-left: 34px; }
  .contact-name { font-weight: 700; font-size: 26px; letter-spacing: 1px; text-transform: uppercase; }
  .contact-title { font-size: 18px; margin-bottom: 14px; color: var(--ink-soft); }
  .contact-list { list-style: none; font-size: 15px; }
  .contact-list li { display: flex; align-items: flex-start; gap: 10px; margin-bottom: 5px; }
  .contact-list .phone { font-weight: 700; font-size: 18px; }
  .contact-list svg { width: 14px; height: 14px; flex: none; margin-top: 3px; fill: var(--ink); }
</style>
</head>
<body>
<main class="sheet">
  <section class="card card-front" aria-label="Card front">
    <div class="elevation-drawing" role="img" aria-label="Faint architectural house elevation drawing in grey line work"></div>
    <div class="wordmark">
      <span class="wordmark-mark"></span>
      <span class="wordmark-name">Veltrow Drafts</span>
    </div>
  </section>

  <section class="card card-back" aria-label="Card back">
    <div class="brand">
      <span class="wordmark-mark"></span>
      <span class="wordmark-name">Veltrow Drafts</span>
    </div>
    <div class="divider"></div>
    <div class="contact">
      <p class="contact-name">Daniel Harlow</p>
      <p class="contact-title">Founder &amp; CEO</p>
      <ul class="contact-list">
        <li class="phone">
          <svg viewBox="0 0 24 24"><path d="M6.6 10.8a15 15 0 0 0 6.6 6.6l2.2-2.2c.3-.3.7-.4 1-.2 1.1.4 2.3.6 3.6.6.6 0 1 .4 1 1V20c0 .6-.4 1-1 1A17 17 0 0 1 3 4c0-.6.4-1 1-1h3.5c.6 0 1 .4 1 1 0 1.3.2 2.5.6 3.6.1.3 0 .7-.2 1z"/></svg>
          (555) 014-2290
        </li>
        <li>
          <svg viewBox="0 0 24 24"><path d="M2 5h20v14H2z M3 6l9 7 9-7" fill="none" stroke="#fff" stroke-width="2"/></svg>
          office@veltrowdrafts.com
        </li>
        <li>
          <svg viewBox="0 0 24 24"><circle cx="12" cy="12" r="9" fill="none" stroke="#fff" stroke-width="2"/><path d="M3 12h18M12 3c3 3 3 15 0 18M12 3c-3 3-3 15 0 18" fill="none" stroke="#fff" stroke-width="1.6"/></svg>
          www.veltrowdrafts.com
        </li>
        <li>
          <svg viewBox="0 0 24 24"><path d="M12 2a7 7 0 0 0-7 7c0 5 7 13 7 13s7-8 7-13a7 7 0 0 0-7-7zm0 9.5A2.5 2.5 0 1 1 12 6.5a2.5 2.5 0 0 1 0 5z"/></svg>
          <span>Your Address, City<br>State, Zip 1235</span>
        </li>
      </ul>
    </div>
  </section>
</main>
</body>
</html>
```